Business needs stationary

We are a company how capital venture and investment webcompany and work for international clients.

We need a stationary for a;

- email template
- business card
- web logo

Use the colors and elements plus company name in the attachment

Business card must include:

- company
- title
- adress
- phonenumber
- email adress
- website adress
- twitter
- facebook

We use the janeausten font. it's free. http://www.glyphtrove.example/mirel-quay.font

```html
<!DOCTYPE html>
<html lang="en">
<head>
<meta charset="utf-8">
<title>Elliot Harlow — Business Card</title>
<link rel="stylesheet" href="https://fonts.googleapis.com/css2?family=Open+Sans:wght@400;700&family=La+Belle+Aurore&display=swap">
<style>
  :root {
    --page: #eeeeec;
    --paper: #fbfbf8;
    --orange: #f76f1a;
    --ink: #2b2b2b;
    --ink-light: #fff6ee;
    --shadow: rgba(0, 0, 0, 0.12);
  }
  * { box-sizing: border-box; margin: 0; padding: 0; }
  html, body {
    width: 1152px;
    height: 1200px;
    overflow: hidden;
    background: var(--page);
  }
  .sheet {
    position: relative;
    width: 1152px;
    height: 1200px;
  }
  .card {
    position: absolute;
    left: 136px;
    width: 880px;
    height: 500px;
    display: flex;
    overflow: hidden;
    box-shadow: 0 10px 30px var(--shadow);
  }
  .card--front { top: 70px; }
  .card--back { top: 630px; }

  .panel { position: relative; width: 50%; height: 100%; }
  .panel--paper { background: var(--paper); }
  .panel--orange { background: var(--orange); }

  .script {
    font-family: "La Belle Aurore", "Segoe Script", "Brush Script MT", cursive;
    color: var(--ink);
    line-height: 1;
    white-space: nowrap;
  }
  .front__first {
    position: absolute;
    left: 90px;
    top: 110px;
    font-size: 104px;
  }
  .front__last {
    position: absolute;
    left: 30px;
    top: 190px;
    font-size: 104px;
  }
  .front__details {
    position: absolute;
    left: 40px;
    top: 340px;
    font-family: "Open Sans", sans-serif;
    color: var(--ink);
  }
  .front__name {
    font-weight: 700;
    font-size: 22px;
    letter-spacing: 1px;
    margin-bottom: 10px;
  }
  .front__contact {
    font-size: 20px;
    letter-spacing: 2px;
    line-height: 1.4;
  }

  .back__address {
    position: absolute;
    left: 50px;
    top: 70px;
    font-family: "Open Sans", sans-serif;
    color: var(--ink-light);
    font-size: 19px;
    letter-spacing: 1.5px;
    line-height: 1.45;
  }
  .back__address .handle { font-weight: 700; }
  .back__address .gap { height: 14px; }

  .back__signature {
    position: absolute;
    left: 110px;
    top: 230px;
    font-size: 60px;
  }
  .back__identity {
    position: absolute;
    left: 110px;
    top: 330px;
    font-family: "Open Sans", sans-serif;
    color: var(--ink);
    font-weight: 700;
    font-size: 19px;
    letter-spacing: 1.5px;
    line-height: 1.45;
  }
  .back__identity .company { font-weight: 400; }
</style>
</head>
<body>
<main class="sheet">
  <section class="card card--front" aria-label="Business card front">
    <div class="panel panel--paper">
      <p class="script front__first">Elliot</p>
    </div>
    <div class="panel panel--orange">
      <p class="script front__last">Harlow</p>
      <div class="front__details">
        <p class="front__name">Elliot Harlow</p>
        <p class="front__contact">www.elliotharlow.example</p>
        <p class="front__contact">(155) 010 427</p>
      </div>
    </div>
  </section>

  <section class="card card--back" aria-label="Business card back">
    <div class="panel panel--orange">
      <div class="back__address">
        <p>Level 7, 218 Wren Lane</p>
        <p>Ashford Bay 4410</p>
        <p>PO Box 382</p>
        <p>Corran Vale 4415</p>
        <div class="gap"></div>
        <p>elliot@elliotharlow.example</p>
        <div class="gap"></div>
        <p>chirpline.example/</p>
        <p class="handle">elliotharlow</p>
        <p>friendboard.example/</p>
        <p class="handle">elliotharlow</p>
      </div>
    </div>
    <div class="panel panel--paper">
      <p class="script back__signature">E Harlow</p>
      <div class="back__identity">
        <p>Elliot Harlow</p>
        <p>CEO</p>
        <p class="company">Elliot Harlow Ventures</p>
      </div>
    </div>
  </section>
</main>
</body>
</html>
```